Postcard Project

I need a postcard designed 6X9 in size printed full color
Will need in the end a high resolution print ready file with crop marks
See instructions in word doc

```html
<!DOCTYPE html>
<html lang="en">
<head>
<meta charset="utf-8">
<title>Drinkware Postcard – Front and Back</title>
<link rel="stylesheet" href="https://fonts.googleapis.com/css2?family=Anton&family=Poppins:wght@400;500;600;700;800&display=swap">
<style>
  :root {
    --red: #c8102e;
    --red-deep: #a3162f;
    --navy: #1d3c78;
    --navy-deep: #263d7c;
    --ink: #1e1e1e;
    --row: #2b2b2d;
    --white: #ffffff;
    --backdrop: #9c9c9c;
  }
  * { box-sizing: border-box; margin: 0; padding: 0; }
  html, body { width: 1147px; height: 1200px; overflow: hidden; }
  body {
    background: var(--backdrop);
    font-family: "Poppins", sans-serif;
    color: var(--ink);
    position: relative;
  }
  .postcard {
    position: absolute;
    left: 168px;
    width: 810px;
    height: 540px;
    background: var(--white);
    overflow: hidden;
    box-shadow: 0 6px 18px rgba(0,0,0,.25);
  }
  .postcard--front { top: 40px; }
  .postcard--back { top: 620px; }
  .backdrop-art { position: absolute; inset: 0; }
  .headline {
    position: absolute;
    font-family: "Anton", sans-serif;
    color: var(--red);
    line-height: 1;
    letter-spacing: -1px;
    transform: skewX(-10deg);
    text-shadow: 2px 2px 0 var(--navy);
    white-space: nowrap;
  }
  .front-headline { left: 30px; top: 14px; font-size: 88px; }
  .back-headline { left: 28px; top: 22px; font-size: 72px; }

  .offer-pill {
    position: absolute; left: 24px; top: 106px; width: 382px; height: 64px;
    background: var(--navy); border-radius: 14px;
    display: flex; align-items: center; padding-left: 6px;
  }
  .offer-pill__amount {
    background: var(--white); color: var(--red);
    height: 52px; border-radius: 26px; padding: 0 14px;
    font-weight: 800; font-size: 38px; line-height: 52px;
  }
  .offer-pill__rest { color: var(--white); font-weight: 500; font-size: 38px; margin-left: 10px; }

  .promo-line { position: absolute; left: 32px; top: 180px; font-size: 15px; font-weight: 500; text-transform: uppercase; white-space: nowrap; }
  .promo-line strong { font-weight: 700; }

  .product-list { position: absolute; left: 67px; top: 204px; width: 290px; list-style: none; }
  .product-list li {
    display: flex; height: 19.5px; margin-bottom: 1.7px;
    background: var(--row); color: var(--white);
    border-radius: 10px; font-size: 11px; line-height: 19.5px; padding-left: 28px;
    white-space: nowrap;
  }
  .product-list .sku { width: 180px; }

  .refer-box {
    position: absolute; left: 0; top: 382px; width: 463px; height: 70px;
    border: 2px solid var(--red); border-left: none; border-radius: 0 36px 36px 0;
    background: var(--white); padding: 4px 0 0 22px;
  }
  .refer-box__title { color: var(--navy); font-weight: 700; font-size: 14.5px; line-height: 1.05; }
  .refer-box__deal { color: var(--red); font-weight: 700; font-size: 14.5px; line-height: 1.05; }
  .refer-box__copy { font-size: 10.5px; line-height: 1.35; margin-top: 2px; }
  .refer-box__copy .hl-red { color: var(--red); font-weight: 600; }
  .refer-box__copy .hl-navy { color: var(--navy); font-weight: 600; }
  .refer-box__code {
    position: absolute; right: 22px; top: 5px; padding-left: 20px;
    border-left: 1.5px solid var(--navy);
    font-family: "Anton", sans-serif; color: var(--red); font-size: 18px; line-height: 1.05;
  }

  .first-order-bar {
    position: absolute; left: 0; top: 461px; width: 463px; height: 60px;
    background: linear-gradient(90deg, var(--red-deep), var(--navy-deep));
    border-radius: 0 30px 30px 0; color: var(--white); padding: 10px 0 0 22px;
    white-space: nowrap;
  }
  .first-order-bar__title { font-weight: 600; font-size: 15px; line-height: 1.3; }
  .first-order-bar__note { font-size: 10.5px; }
  .first-order-bar__note strong { font-size: 14px; font-weight: 700; }

  .photo-person {
    position: absolute; left: 468px; top: 14px; width: 320px; height: 300px;
    background: radial-gradient(ellipse at 55% 30%, #d6bfa6 0%, #c9b8a2 30%, #5f7f92 60%, #ebebeb 100%);
    border-radius: 46% 46% 0 0;
  }
  .photo-products {
    position: absolute; left: 470px; top: 305px; width: 330px; height: 220px;
    background: linear-gradient(90deg, #c62b2b 0%, #2346a6 22%, #f2f2f2 45%, #cfd2d6 65%, #d52424 80%, #c9b89a 100%);
    border-radius: 10px;
  }

  .referral-panel {
    position: absolute; left: 23px; top: 113px; width: 312px; height: 140px;
    border: 2px solid var(--navy); border-radius: 14px; overflow: hidden;
    background: linear-gradient(180deg, var(--red-deep) 0%, #6b2b5a 60%, var(--navy-deep) 100%);
    color: var(--white); text-align: center;
  }
  .referral-panel__head { font-weight: 700; font-size: 16px; line-height: 1.1; padding: 6px 0; border-bottom: 1px solid rgba(255,255,255,.6); }
  .referral-panel__cols { display: flex; height: 94px; }
  .referral-panel__col { flex: 1; font-size: 11.5px; line-height: 1.35; padding-top: 5px; }
  .referral-panel__col + .referral-panel__col { border-left: 1px solid rgba(255,255,255,.7); }
  .referral-panel__col strong { font-weight: 700; }
  .referral-panel__min { display: block; font-weight: 700; font-size: 15px; margin-top: 10px; }
  .promo-tab {
    position: absolute; left: 87px; top: 257px; width: 184px; height: 30px;
    background: var(--red); color: var(--white);
    font-family: "Anton", sans-serif; font-size: 19px; line-height: 30px; text-align: center;
    border-radius: 0 0 6px 6px;
  }
  .back-products { left: 18px; top: 303px; width: 330px; height: 222px; }
  .stamp-box { position: absolute; left: 675px; top: 21px; width: 113px; height: 130px; border: 1.5px solid var(--ink); }
  .address-line { position: absolute; left: 464px; width: 324px; height: 0; border-top: 1.2px solid var(--ink); }
</style>
</head>
<body>

<section class="postcard postcard--front" aria-label="Postcard front">
  <svg class="backdrop-art" viewBox="0 0 810 540" preserveAspectRatio="none" aria-hidden="true">
    <defs>
      <linearGradient id="frontMist" x1="0" y1="0" x2="1" y2="0">
        <stop offset="0" stop-color="#ffffff"/>
        <stop offset="1" stop-color="#e4e4e6"/>
      </linearGradient>
    </defs>
    <polygon points="0,0 810,0 810,380 0,196" fill="url(#frontMist)"/>
    <polygon points="0,196 810,380 810,392 0,208" fill="#c8102e"/>
  </svg>

  <div class="photo-person" role="img" aria-label="Smiling man giving a thumbs gesture while holding a red tumbler"></div>
  <div class="photo-products" role="img" aria-label="Group of drinkware: bottles, tumblers, mugs and cups in red, blue, white and black"></div>

  <h1 class="headline front-headline">DRINKWARE</h1>

  <div class="offer-pill">
    <span class="offer-pill__amount">$50 OFF</span>
    <span class="offer-pill__rest">ON YOUR</span>
  </div>

  <p class="promo-line">Use promo code: <strong>DRINK (Valid until 9/30/25)</strong></p>

  <ul class="product-list">
    <li><span class="sku">DW-2041SL_B_BACK</span><span>Black</span></li>
    <li><span class="sku">DW-2052WH_A_BACK</span><span>Full Color</span></li>
    <li><span class="sku">DW-2063RD_B_BACK</span><span>White</span></li>
    <li><span class="sku">DW-2074BK_B_FR_3310</span><span>White</span></li>
    <li><span class="sku">DW-2085WH_B_FR_4421</span><span>Full</span></li>
    <li><span class="sku">TK-3011RD_B_FR</span><span>Black</span></li>
    <li><span class="sku">TK-3027RBL_B__5532</span><span>White</span></li>
    <li><span class="sku">TK-3049WH_B_FR_6614</span><span>Black</span></li>
  </ul>

  <div class="refer-box">
    <p class="refer-box__title">REFER a Friend</p>
    <p class="refer-box__deal">GIVE $100, GET $100</p>
    <p class="refer-box__copy">Give your friends <span class="hl-red">$100</span> off their first purchase <span class="hl-navy">(over $500)</span><br>and receive a <span class="hl-red">$100</span> discount on any order <span class="hl-navy">(over $500)</span>.</p>
    <p class="refer-box__code">PROMO<br>CODE<br>REFER</p>
  </div>

  <div class="first-order-bar">
    <p class="first-order-bar__title">$150 Off Your First Department Purchase of $500</p>
    <p class="first-order-bar__note">Use Promo Code: <strong>FIRST150</strong> (This offer cannot be combined with others)</p>
  </div>
</section>

<section class="postcard postcard--back" aria-label="Postcard back">
  <svg class="backdrop-art" viewBox="0 0 810 540" preserveAspectRatio="none" aria-hidden="true">
    <defs>
      <linearGradient id="backMist" x1="0" y1="0" x2="1" y2="0">
        <stop offset="0" stop-color="#f4f4f5"/>
        <stop offset="1" stop-color="#ffffff"/>
      </linearGradient>
    </defs>
    <polygon points="0,0 349,0 440,266 349,540 0,540" fill="url(#backMist)"/>
    <polyline points="352,-4 442,266 352,544" fill="none" stroke="#c8102e" stroke-width="8"/>
  </svg>

  <h2 class="headline back-headline">DRINKWARE</h2>

  <div class="referral-panel">
    <p class="referral-panel__head">REFER a Friend<br>GIVE $100, GET $100</p>
    <div class="referral-panel__cols">
      <p class="referral-panel__col">Give your friends<br><strong>$100 off</strong> their<br>first purchase<span class="referral-panel__min">(over $500)</span></p>
      <p class="referral-panel__col">Receive a<br><strong>$100 discount</strong><br>on any order<span class="referral-panel__min">(over $500)</span></p>
    </div>
  </div>
  <div class="promo-tab">PROMO CODE REFER</div>

  <div class="photo-products back-products" role="img" aria-label="Group of drinkware: bottles, tumblers, mugs and cups in red, blue, white and black"></div>

  <div class="stamp-box" aria-label="Stamp area"></div>
  <div class="address-line" style="top:271px"></div>
  <div class="address-line" style="top:333px"></div>
  <div class="address-line" style="top:396px"></div>
  <div class="address-line" style="top:460px"></div>
</section>

</body>
</html>
```